We need a wordpress website design (preferably using canvas theme) for a new company called Copper Ridge Analytics (CRA). CRA is a business to business site that provides information, news, and data about the medical marijuana industry. The site will have a home page/dashboard that highlights the top news, featured companies, featured people, and featured reports. The site will also have profile pages that contain detailed information about companies, people, events, and states (regulations). The site will also have a woo commerce store for reports and data extracts.
Note: In general, we are using Calibri for logo and header fonts. A readable sans serif for text. Copper Ridge Blue: RGB: 3 56 121 HEX: 033879
We can also use complimentary green accents, and shades of blue and grey around it as accent.
Updates

Target Market(s)

- Professional, entrepreneurial men 29-55 years old. They are young high net worth investors, lawyers, entrepreneurs and in the financial sector – or they strive to be there.
- They read Brisk Venture, Harbor Lane Gazette, Capital Markets Weekly, hempledgerwire.example (they wish it were better). They visit the site sproutlo.example
- they follow us on twitter and facebook.

Industry/Entity Type

Medical

Font styles to use
Sans Serif

Colors
0255a3
acd036
3176b5
85acd3
eaf1f7

Requirements
Must have
• Widgets on the home page may include stock feeds, as well as groups of information such as events and featured people.

User must have ability to see featured reports including cover art and brief (one line) summary so they can go purchase them in the store. Once in the store, they can preview a longer abstract (~50-200 words). User will want to know length of report in pages before they buy
Nice to have
• Lots of images throughout the site, for instance images that are associated with each report. those images may be the cover art. Also images associated with the people, events, etc. These will typically be profile pics and company logos.
Should not have
• Although this is a medical marijuana site, we do not want to have graphics, images, or icons that show marijuana leaves or flowers.

```html
<!DOCTYPE html>
<html lang="en">
<head>
<meta charset="utf-8">
<title>Copper Ridge Analytics</title>
<link rel="stylesheet" href="https://fonts.googleapis.com/css2?family=Open+Sans:ital,wght@0,400;0,600;0,700;1,600;1,700&display=swap">
<style>
:root{
  --brand:#033879;
  --blue:#0255a3;
  --blue-mid:#3176b5;
  --blue-soft:#85acd3;
  --blue-pale:#eaf1f7;
  --green:#acd036;
  --amber:#f6b42c;
  --grey-card:#e4e4e4;
  --grey-band:#ececec;
  --text:#555;
  --line:#d6d6d6;
}
*{margin:0;padding:0;box-sizing:border-box}
html,body{width:1200px;height:2264px;overflow:hidden;background:#fff}
body{font-family:"Open Sans",sans-serif;color:var(--text);position:relative}
.abs{position:absolute}
.ph{position:absolute;display:block}

/* header */
.topbar{left:0;top:0;width:1200px;height:68px;background:rgba(37,96,170,.88);z-index:3}
.logo{left:88px;top:0;width:267px;height:88px;background:#fff;z-index:4;display:flex;align-items:center;justify-content:center;gap:9px;box-shadow:0 2px 4px rgba(0,0,0,.15)}
.logo-dot{width:20px;height:20px;border-radius:50%;background:var(--brand)}
.logo-name{font-size:19px;font-weight:600;color:var(--brand);letter-spacing:-.4px}
.main-nav{left:388px;top:0;height:68px;display:flex;align-items:center;gap:26px;z-index:4}
.main-nav a{color:#cfe0f2;font-size:13px;text-decoration:none;text-transform:uppercase}
.main-nav a.on{color:#fff}
.btn-login,.btn-register{top:0;height:68px;display:flex;align-items:center;justify-content:center;color:#fff;font-size:13px;text-transform:uppercase;z-index:4}
.btn-login{left:946px;width:72px;background:var(--green)}
.btn-register{left:1020px;width:92px;background:var(--blue-soft)}
.hero{left:0;top:0;width:1200px;height:524px;background:linear-gradient(100deg,#a9c9e0 0%,#d9e7f0 35%,#c6d6e2 60%,#7fa8c8 100%)}

/* shared */
.meta{font-size:11.5px;color:#777;text-transform:uppercase;display:flex;gap:26px}
.title{font-size:13px;color:var(--blue);font-weight:600;line-height:17px}
.section-head{font-size:17px;font-weight:700;color:var(--blue);text-transform:uppercase}
.rule-h{height:1px;background:var(--line)}
.rule-v{width:1px;background:var(--line)}

/* report cards */
.report{width:310px;height:172px}
.report .ph{left:0;top:0;width:100%;height:100%}
.badge{position:absolute;left:0;top:0;width:52px;height:56px;color:#fff;text-align:center;padding-top:6px}
.badge b{display:block;font-size:20px;line-height:22px;font-weight:700}
.badge span{font-size:12px}
.badge.blue{background:var(--blue-mid)}
.badge.green{background:var(--green)}
.report .cap{position:absolute;left:0;bottom:0;width:100%;height:36px;background:rgba(20,40,70,.65);color:#fff;font-size:13px;font-weight:600;padding:9px 12px}
.report .cap.lime{color:var(--green)}

/* events */
.event{width:205px;height:248px;background:var(--grey-card)}
.event .ph{left:0;top:0;width:205px;height:135px}
.event h4{position:absolute;left:16px;top:150px;width:180px;font-size:13px;font-weight:600;color:#333;line-height:17px}
.event h4.blue{color:var(--blue)}
.event p{position:absolute;left:16px;top:204px;width:180px;font-size:11.5px;line-height:17px;color:#888}

/* news */
.news{left:804px;width:308px;height:80px;background:var(--grey-card)}
.news .txt{position:absolute;left:13px;top:10px}
.news .date{font-size:11px;font-style:italic;font-weight:700;color:#333}
.news .head{font-size:12.5px;font-weight:600;color:var(--blue);margin-top:4px}
.news .more{font-size:10.5px;color:#999;margin-top:6px}
.news .ph{right:0;top:0;width:118px;height:80px}
.news.lead{background:var(--blue)}
.news.lead .ph{left:0;right:auto}
.news.lead .txt{left:130px}
.news.lead .date,.news.lead .head,.news.lead .more{color:#fff}

/* charts */
.chart-title{left:804px;width:308px;text-align:center;font-size:15px;color:#111}

/* footer */
.footer-band{left:0;top:2122px;width:1200px;height:89px;background:var(--grey-band)}
.signup{left:97px;top:2146px;width:263px;height:39px;background:#fff;display:flex;align-items:center}
.signup .lbl{font-size:11px;color:#333;padding:0 12px;border-right:1px solid #ddd;line-height:20px}
.signup .field{font-size:10px;color:#aaa;padding-left:12px;flex:1;letter-spacing:.5px}
.signup .go{width:39px;height:39px;border:2px solid var(--blue);display:flex;align-items:center;justify-content:center}
.copy{left:450px;top:2146px;width:300px;text-align:center;font-size:11.5px;color:#333}
.copy em{font-style:normal;color:var(--blue)}
.copy small{display:block;font-size:9px;margin-top:5px}
.social{left:912px;top:2156px;display:flex;gap:12px}
.social i{display:block;width:20px;height:20px;background:#b8b8b8}
.social i.first{background:var(--brand)}
.bottom-nav{left:0;top:2211px;width:1200px;height:53px;background:var(--blue);display:flex;align-items:center;justify-content:center;font-size:12.5px;text-transform:uppercase}
.bottom-nav a{color:#cfe0f2;text-decoration:none;padding:0 12px;border-left:1px solid #3f7cbd;line-height:12px}
.bottom-nav a:first-child{border-left:none;color:#fff}
</style>
</head>
<body>

<div class="ph hero" role="img" aria-label="Photo of a scientist in a lab coat and safety glasses pipetting in a laboratory"></div>
<div class="abs topbar"></div>
<div class="abs logo"><span class="logo-dot"></span><span class="logo-name">Copper Ridge Analytics</span></div>
<nav class="abs main-nav">
  <a class="on" href="#">Home</a><a href="#">About Us</a><a href="#">People</a><a href="#">Events</a><a href="#">States</a><a href="#">News</a><a href="#">Contact Us</a>
</nav>
<div class="abs btn-login">Login</div>
<div class="abs btn-register">Register</div>

<!-- featured articles -->
<div class="ph" style="left:88px;top:564px;width:309px;height:171px;background:linear-gradient(180deg,#8a9a6a,#5c7a32)" role="img" aria-label="Photo of a greenhouse crop under grow lights"></div>
<div class="ph" style="left:430px;top:564px;width:310px;height:171px;background:linear-gradient(180deg,#3c74c8,#8fb4e2 70%,#6e8a5a)" role="img" aria-label="Photo of wind turbines under a blue sky"></div>
<div class="abs meta" style="left:88px;top:745px"><span>Lorem ipsum</span><span>|</span><span>July 11, 2014</span></div>
<div class="abs meta" style="left:430px;top:745px"><span>Lorem ipsum</span><span>|</span><span>July 11, 2014</span></div>
<div class="abs title" style="left:88px;top:769px;width:315px">Lorem ipsum dolor sit amet, coctetur adipiscing elit</div>
<div class="abs title" style="left:430px;top:769px;width:315px">Lorem ipsum dolor sit amet, coctetur adipiscing elit</div>

<div class="ph" style="left:88px;top:830px;width:652px;height:318px;background:linear-gradient(120deg,#0d3a3a,#1f6a62 50%,#0e3e40)" role="img" aria-label="Photo of a researcher in front of glowing chemical formulas"></div>
<div class="abs meta" style="left:88px;top:1158px"><span>Lorem ipsum</span><span>|</span><span>July 11, 2014</span></div>
<div class="abs title" style="left:88px;top:1181px;width:652px;font-size:14px;line-height:19px">Lorem ipsum dolor sit amet, consectetur adipiscing elit. Ut consequat erat dolor, eu mollis arcu rhoncus ut. Donec cursus ultrices ante.</div>
<p class="abs" style="left:88px;top:1224px;width:652px;font-size:11px;line-height:20px;color:#666">Etiam sed pellentesque ante, porta aliquet nibh. Duis ac turpis vel ipsum feugiat blandit. Nulla egestas cursus nisi quis tincidunt. Phasellus pretium sapien id quam rhoncus, porta faucibus leo elementum. Sed sapien quam, dignissim vitae nisi et, sodales malesuada turpis.</p>

<div class="abs rule-h" style="left:88px;top:1312px;width:683px"></div>
<div class="abs rule-v" style="left:771px;top:560px;height:1523px"></div>

<!-- research reports -->
<h2 class="abs section-head" style="left:88px;top:1337px">Research Reports</h2>
<div class="abs report" style="left:88px;top:1372px">
  <div class="ph" style="background:linear-gradient(135deg,#2aa9c9,#7fd0e0 50%,#2d5f8c)" role="img" aria-label="Photo of an eye scan on a digital screen"></div>
  <div class="badge blue"><b>30</b><span>APR</span></div>
  <div class="cap" style="background:rgba(40,110,180,.8)">Lorem ipsum dolor sit amet adip edit</div>
</div>
<div class="abs report" style="left:430px;top:1372px">
  <div class="ph" style="background:linear-gradient(180deg,#5f9ee0,#c9dcef 45%,#3b5877)" role="img" aria-label="Photo of solar panels under clouds"></div>
  <div class="badge green"><b>30</b><span>APR</span></div>
  <div class="cap lime">Lorem ipsum dolor sit amet adip edit</div>
</div>
<div class="abs report" style="left:88px;top:1577px">
  <div class="ph" style="background:linear-gradient(135deg,#cfe3f1,#6fa3d6 55%,#e7eef4)" role="img" aria-label="Photo of a hand holding a tablet showing charts"></div>
  <div class="badge green"><b>30</b><span>APR</span></div>
  <div class="cap lime">Lorem ipsum dolor sit amet adip edit</div>
</div>
<div class="abs report" style="left:430px;top:1577px">
  <div class="ph" style="background:linear-gradient(135deg,#d6844a,#9a5a6a 60%,#5a3f66)" role="img" aria-label="Photo of glasses resting on printed financial charts"></div>
  <div class="badge green"><b>30</b><span>APR</span></div>
  <div class="cap lime">Lorem ipsum dolor sit amet adip edit</div>
</div>

<div class="abs rule-h" style="left:88px;top:1781px;width:683px"></div>

<!-- top events -->
<h2 class="abs section-head" style="left:88px;top:1805px">Top Events</h2>
<div class="abs event" style="left:88px;top:1837px">
  <div class="ph" style="background:linear-gradient(135deg,#e08a4a,#b8623a)" role="img" aria-label="Photo of glasses on printed charts"></div>
  <div class="badge blue" style="top:79px"><b>30</b><span>APR</span></div>
  <h4 class="blue">Lorem ipsum dolor sit ame dolor</h4>
  <p>Consectetur adipis Maecenas aliquet velit in lacus</p>
</div>
<div class="abs event" style="left:311px;top:1837px">
  <div class="ph" style="background:radial-gradient(circle at 50% 50%,#fff 0,#bcd6f3 25%,#2c64b8 70%)" role="img" aria-label="Photo of sunlight over solar panels"></div>
  <div class="badge green" style="top:79px"><b>30</b><span>APR</span></div>
  <h4>Lorem ipsum dolor amet dolor</h4>
  <p>Consectetur adipis Maecenas aliquet velit in lacus</p>
</div>
<div class="abs event" style="left:534px;top:1837px">
  <div class="ph" style="background:linear-gradient(135deg,#e4ecf2,#b9c9d6 60%,#8a9aa8)" role="img" aria-label="Photo of a business meeting in a bright office"></div>
  <div class="badge green" style="top:79px"><b>30</b><span>APR</span></div>
  <h4>Lorem ipsum dolor amet dolor</h4>
  <p>Consectetur adipis Maecenas aliquet velit in lacus</p>
</div>

<!-- sidebar -->
<h2 class="abs section-head" style="left:804px;top:559px">Latest News</h2>
<div class="abs news lead" style="top:590px">
  <div class="ph" style="background:linear-gradient(135deg,#dfe8ef,#9fb2c2)" role="img" aria-label="Photo of colleagues at a meeting"></div>
  <div class="txt"><div class="date">JUL 10, 2014</div><div class="head">Lorem ispum dolor amet</div><div class="more">Read more</div></div>
</div>
<div class="abs news" style="top:673px">
  <div class="txt"><div class="date">JUL 10, 2014</div><div class="head">Lorem ispum dolor amet</div><div class="more">Read more</div></div>
  <div class="ph" style="background:linear-gradient(135deg,#e08a4a,#a0583a)" role="img" aria-label="Photo of glasses on charts"></div>
</div>
<div class="abs news" style="top:756px">
  <div class="txt"><div class="date">JUL 10, 2014</div><div class="head">Lorem ispum dolor amet</div><div class="more">Read more</div></div>
  <div class="ph" style="background:radial-gradient(circle at 50% 45%,#fff 0,#a8caf0 30%,#1f56a8 75%)" role="img" aria-label="Photo of sunlight over solar panels"></div>
</div>
<div class="abs news" style="top:839px">
  <div class="txt"><div class="date">JUL 10, 2014</div><div class="head">Lorem ispum dolor amet</div><div class="more">Read more</div></div>
  <div class="ph" style="background:linear-gradient(180deg,#c9d8a0,#9aaa5a)" role="img" aria-label="Photo of a person walking through a field"></div>
</div>
<div class="abs news" style="top:922px">
  <div class="txt"><div class="date">JUL 10, 2014</div><div class="head">Lorem ispum dolor amet</div><div class="more">Read more</div></div>
  <div class="ph" style="background:linear-gradient(135deg,#eef0f2,#b7bcc2)" role="img" aria-label="Photo of two businesspeople talking"></div>
</div>

<!-- bar chart widget -->
<svg class="abs" style="left:804px;top:1035px" width="308" height="233" viewBox="0 0 308 233" font-family="Open Sans, sans-serif">
  <rect x=".5" y=".5" width="307" height="232" fill="#fff" stroke="#cfd8e2"/>
  <text x="16" y="24" font-size="11" fill="#033879" font-weight="700">Licensed Dispensaries</text>
  <text x="292" y="24" font-size="9" fill="#777" text-anchor="end">by quarter</text>
  <g stroke="#ececec">
    <line x1="36" y1="50" x2="292" y2="50"/><line x1="36" y1="85" x2="292" y2="85"/><line x1="36" y1="120" x2="292" y2="120"/><line x1="36" y1="155" x2="292" y2="155"/>
  </g>
  <line x1="36" y1="190" x2="292" y2="190" stroke="#999"/>
  <g font-size="7.5" fill="#666" text-anchor="end">
    <text x="30" y="53">400</text><text x="30" y="88">300</text><text x="30" y="123">200</text><text x="30" y="158">100</text><text x="30" y="193">0</text>
  </g>
  <g fill="#3176b5">
    <rect x="48" y="148" width="18" height="42"/><rect x="80" y="134" width="18" height="56"/><rect x="112" y="141" width="18" height="49"/><rect x="144" y="116" width="18" height="74"/><rect x="176" y="102" width="18" height="88"/><rect x="208" y="88" width="18" height="102"/><rect x="240" y="71" width="18" height="119"/>
  </g>
  <rect x="272" y="60" width="14" height="130" fill="#acd036"/>
  <g font-size="7.5" fill="#666" text-anchor="middle">
    <text x="57" y="204">Q1</text><text x="89" y="204">Q2</text><text x="121" y="204">Q3</text><text x="153" y="204">Q4</text><text x="185" y="204">Q1</text><text x="217" y="204">Q2</text><text x="249" y="204">Q3</text><text x="279" y="204">Q4</text>
  </g>
  <text x="100" y="221" font-size="7.5" fill="#999" text-anchor="middle">2013</text>
  <text x="232" y="221" font-size="7.5" fill="#999" text-anchor="middle">2014</text>
</svg>

<!-- pie chart widget -->
<div class="abs chart-title" style="top:1296px">Exploded Pie Slice Chart</div>
<svg class="abs" style="left:804px;top:1320px" width="308" height="207" viewBox="0 0 308 207" font-family="Open Sans, sans-serif">
  <rect x=".5" y=".5" width="307" height="206" fill="#fff" stroke="#555"/>
  <g stroke="#fff" stroke-width="1.5">
    <path d="M112,104 L112,34 A70,70 0 0 1 178.6,82.4 Z" fill="#0255a3"/>
    <path d="M112,104 L178.6,82.4 A70,70 0 0 1 153.1,160.6 Z" fill="#3176b5"/>
    <path d="M112,104 L153.1,160.6 A70,70 0 0 1 70.9,160.6 Z" fill="#85acd3"/>
    <path d="M112,104 L70.9,160.6 A70,70 0 0 1 45.4,82.4 Z" fill="#b9d0e6"/>
    <path d="M104,99 L37.4,77.4 A70,70 0 0 1 104,29 Z" fill="#acd036"/>
  </g>
  <g font-size="8" fill="#333">
    <rect x="210" y="62" width="8" height="8" fill="#0255a3"/><text x="223" y="69">Medical</text>
    <rect x="210" y="78" width="8" height="8" fill="#3176b5"/><text x="223" y="85">Cultivation</text>
    <rect x="210" y="94" width="8" height="8" fill="#85acd3"/><text x="223" y="101">Testing</text>
    <rect x="210" y="110" width="8" height="8" fill="#b9d0e6"/><text x="223" y="117">Ancillary</text>
    <rect x="210" y="126" width="8" height="8" fill="#acd036"/><text x="223" y="133">Research</text>
  </g>
</svg>

<!-- program ad -->
<div class="abs" style="left:804px;top:1559px;width:308px;height:284px;background:linear-gradient(180deg,#1c8fd6,#0f6fb8)">
  <div class="ph" style="left:120px;top:50px;width:188px;height:234px;background:linear-gradient(180deg,rgba(255,255,255,0),rgba(255,255,255,.18))" role="img" aria-label="Illustration of a person with arms outstretched"></div>
  <div class="abs" style="left:16px;top:12px;font-size:33px;font-weight:700;color:#fff">The Program</div>
  <div class="abs" style="left:16px;top:154px;font-size:13.5px;font-weight:700;color:#fff;line-height:24px">All your arthritis news<br>and information.<br>All the time.</div>
  <div class="abs" style="left:16px;top:238px;font-size:19px;font-weight:700;color:#fff">Learn more&gt;</div>
</div>

<div class="ph" style="left:804px;top:1874px;width:308px;height:148px;background:linear-gradient(120deg,#2f7fd0,#8fc3ea 55%,#e8eef2)" role="img" aria-label="Photo of a gloved hand holding a test tube containing a globe"></div>

<!-- footer -->
<div class="abs footer-band"></div>
<div class="abs signup"><span class="lbl">SIGN UP</span><span class="field">EMAIL ADDRESS</span>
  <span class="go"><svg width="16" height="10" viewBox="0 0 16 10"><path d="M0 5H14M10 1L14 5L10 9" fill="none" stroke="#0255a3" stroke-width="1.5"/></svg></span>
</div>
<div class="abs copy">© 2014 <em>COPPER RIDGE ANALYTICS</em><small>PRIVACY POLICY | TERMS OF USE</small></div>
<div class="abs social"><i class="first"></i><i></i><i></i><i></i><i></i><i></i></div>
<nav class="abs bottom-nav">
  <a href="#">Home</a><a href="#">About Us</a><a href="#">People</a><a href="#">Events</a><a href="#">States</a><a href="#">News</a><a href="#">Featured Companies</a><a href="#">Featured People</a><a href="#">Featured Reports</a><a href="#">Contact Us</a>
</nav>

</body>
</html>
```